Nana Bee's needs your help creating a clean, simple, possibly vintage style label for a natural rem...

We need a label for a new product to be sold in local stores. It will be a bottle of fresh Elderberry Syrup which is a natural remedy for the flu, colds, and allergies. Our syrup is different from others in the market as it is fresh, needs to be refrigerated, and does not include preservatives, added sugar, alcohol, or anything artificial. We would like a label with easy to read text, with a clean or vintage look. We would like a 3 inch by 3 inch circle front label with mostly text, not too busy, and possibly a branch of elderberries may be included. We also need a 3 inch by 3 inch circle label for the back of the bottle with the nutrition facts, ingredients, dosage, and specific text. Both labels should be lighter in (background) color to stand out from the dark purple liquid inside. We're leaning towards black for the main text, but open to other ideas that are neutral and not too flashy.The final design should be clear, clean, making the main text visible if in a grocery store refrigerator. It should appeal to all, but mostly to natural minded mothers.
Target Market(s)
Natural minded mothers

```html
<!DOCTYPE html>
<html lang="en">
<head>
<meta charset="utf-8">
<title>Nana Bee's Elderberry Syrup – Front Label Options</title>
<link rel="stylesheet" href="https://fonts.googleapis.com/css2?family=Oswald:wght@500;600&family=Bebas+Neue&family=Yellowtail&family=Dancing+Script:wght@700&family=Great+Vibes&family=Rye&family=Roboto+Slab:wght@700&family=Old+Standard+TT:wght@700&display=swap">
<style>
  :root {
    --page: #ffffff;
    --ink: #1d1a18;
    --kraft-light: #f0d6b4;
    --kraft: #e6c39a;
    --kraft-edge: #dcb68a;
    --branch: #b48a62;
  }
  html, body {
    margin: 0;
    padding: 0;
    width: 1200px;
    height: 1200px;
    overflow: hidden;
    background: var(--page);
  }
  .sheet { display: block; width: 1200px; height: 1200px; }
  .ring-outer { fill: none; stroke: var(--ink); stroke-width: 1.3; }
  .ring-inner { fill: none; stroke: var(--ink); stroke-width: 2.6; }
  .arc-text { font-family: 'Oswald', sans-serif; font-weight: 500; font-size: 17px; fill: var(--ink); }
  .net-text { font-family: 'Oswald', sans-serif; font-weight: 500; font-size: 11px; fill: var(--ink); }
  .dot { fill: var(--ink); }
  .tagline { font-family: 'Oswald', sans-serif; font-weight: 500; font-size: 10px; fill: var(--ink); letter-spacing: 0.3px; }
  .brand { fill: var(--ink); }
  .brand--casual { font-family: 'Dancing Script', cursive; font-size: 36px; }
  .brand--flowing { font-family: 'Yellowtail', cursive; font-size: 38px; }
  .brand--fine { font-family: 'Great Vibes', cursive; font-size: 40px; }
  .product { fill: var(--ink); }
  .product--serif { font-family: 'Old Standard TT', serif; font-weight: 700; font-size: 34px; }
  .product--condensed { font-family: 'Bebas Neue', sans-serif; font-size: 52px; }
  .product--gothic { font-family: 'Oswald', sans-serif; font-weight: 600; font-size: 38px; }
  .product--slab { font-family: 'Roboto Slab', serif; font-weight: 700; font-size: 31px; }
  .product--western { font-family: 'Rye', serif; font-size: 31px; }
  .format { fill: var(--ink); }
  .format--serif { font-family: 'Old Standard TT', serif; font-weight: 700; font-size: 22px; letter-spacing: 4px; }
  .format--sans { font-family: 'Oswald', sans-serif; font-weight: 500; font-size: 25px; letter-spacing: 4px; }
</style>
</head>
<body>
<svg class="sheet" viewBox="0 0 1200 1200" xmlns="http://www.w3.org/2000/svg">
  <defs>
    <radialGradient id="kraftFill" cx="50%" cy="45%" r="55%">
      <stop offset="0%" stop-color="var(--kraft-light)"/>
      <stop offset="80%" stop-color="var(--kraft)"/>
      <stop offset="100%" stop-color="var(--kraft-edge)"/>
    </radialGradient>
    <path id="topArc" d="M -102.2,59 A118 118 0 1 1 102.2,59"/>
    <path id="bottomArc" d="M -60,107.8 A123.4 123.4 0 0 0 60,107.8"/>

    <g id="labelBase">
      <circle r="150" fill="url(#kraftFill)"/>
      <circle class="ring-outer" r="143"/>
      <circle class="ring-inner" r="139"/>
      <text class="arc-text"><textPath href="#topArc" textLength="490" lengthAdjust="spacing">MADE WITH ORGANIC ELDERBERRIES &amp; SPICES &amp; LOCAL TEXAS RAW HONEY</textPath></text>
      <text class="net-text"><textPath href="#bottomArc" startOffset="50%" text-anchor="middle">NET WT 8 FL OZ</textPath></text>
      <circle class="dot" cx="-70" cy="100" r="2.6"/>
      <circle class="dot" cx="70" cy="100" r="2.6"/>
      <text class="tagline" x="0" y="56" text-anchor="middle">IMMUNE BOOSTING</text>
      <ellipse cx="0" cy="84" rx="34" ry="20" fill="var(--branch)" role="img" aria-label="Illustration of an elderberry branch with leaves and berry clusters"/>
    </g>
  </defs>

  <!-- Row one -->
  <g class="label" transform="translate(160 431) scale(0.86)">
    <use href="#labelBase"/>
    <text class="brand brand--casual" x="0" y="-48" text-anchor="middle">Nana Bee's</text>
    <text class="product product--serif" x="0" y="0" text-anchor="middle" textLength="212" lengthAdjust="spacingAndGlyphs">ELDERBERRY</text>
    <text class="format format--serif" x="0" y="36" text-anchor="middle">SYRUP</text>
  </g>

  <g class="label" transform="translate(461 431) scale(0.86)">
    <use href="#labelBase"/>
    <text class="brand brand--flowing" x="0" y="-52" text-anchor="middle">Nana Bee's</text>
    <text class="product product--condensed" x="0" y="6" text-anchor="middle" textLength="206" lengthAdjust="spacingAndGlyphs">ELDERBERRY</text>
    <text class="format format--sans" x="0" y="38" text-anchor="middle">SYRUP</text>
  </g>

  <g class="label" transform="translate(753 431) scale(0.86)">
    <use href="#labelBase"/>
    <text class="brand brand--fine" x="0" y="-50" text-anchor="middle">Nana Bee's</text>
    <text class="product product--gothic" x="0" y="-2" text-anchor="middle" textLength="212" lengthAdjust="spacingAndGlyphs">ELDERBERRY</text>
    <text class="format format--sans" x="0" y="36" text-anchor="middle">SYRUP</text>
  </g>

  <g class="label" transform="translate(1045 431) scale(0.86)">
    <use href="#labelBase"/>
    <text class="brand brand--flowing" x="0" y="-44" text-anchor="middle">Nana Bee's</text>
    <text class="product product--slab" x="0" y="-4" text-anchor="middle" textLength="222" lengthAdjust="spacingAndGlyphs">ELDERBERRY</text>
    <text class="format format--serif" x="0" y="34" text-anchor="middle">SYRUP</text>
  </g>

  <!-- Row two -->
  <g class="label" transform="translate(160 820) scale(0.86)">
    <use href="#labelBase"/>
    <text class="brand brand--casual" x="0" y="-52" text-anchor="middle">Nana Bee's</text>
    <text class="product product--serif" x="0" y="-2" text-anchor="middle" textLength="212" lengthAdjust="spacingAndGlyphs">ELDERBERRY</text>
    <text class="format format--serif" x="0" y="34" text-anchor="middle">SYRUP</text>
  </g>

  <g class="label" transform="translate(461 820) scale(0.86)">
    <use href="#labelBase"/>
    <text class="brand brand--casual" x="0" y="-52" text-anchor="middle">Nana Bee's</text>
    <text class="product product--western" x="0" y="-4" text-anchor="middle" textLength="210" lengthAdjust="spacingAndGlyphs">ElderBerry</text>
    <text class="format format--sans" x="0" y="34" text-anchor="middle">SYRUP</text>
  </g>

  <g class="label" transform="translate(753 820) scale(0.86)">
    <use href="#labelBase"/>
    <text class="brand brand--casual" x="0" y="-52" text-anchor="middle">Nana Bee's</text>
    <text class="product product--western" x="0" y="-4" text-anchor="middle" textLength="218" lengthAdjust="spacingAndGlyphs">ElderBerry</text>
    <text class="format format--sans" x="0" y="34" text-anchor="middle">SYRUP</text>
  </g>

  <g class="label" transform="translate(1045 820) scale(0.86)">
    <use href="#labelBase"/>
    <text class="brand brand--casual" x="0" y="-54" text-anchor="middle">Nana Bee's</text>
    <text class="product product--gothic" x="0" y="-4" text-anchor="middle" textLength="212" lengthAdjust="spacingAndGlyphs">ELDERBERRY</text>
    <text class="format format--serif" x="0" y="38" text-anchor="middle">SYRUP</text>
  </g>
</svg>
</body>
</html>
```